I need a business card for ALVA Holdings. We are a young startup based in New Zealand working in internet marketing and web development. The design should have some element connected to New Zealand, such as wave, koru or silver fern, just don't use a kiwi bird.

```html
<!DOCTYPE html>
<html lang="en">
<head>
<meta charset="utf-8">
<title>ALVA Holdings – Business Card</title>
<link href="https://fonts.googleapis.com/css2?family=Montserrat:wght@700&family=Roboto:wght@400;500&display=swap" rel="stylesheet">
<style>
  :root {
    --bg: #9c9c9c;
    --blue: #1a75c4;
    --orange: #f05a28;
    --white: #ffffff;
  }
  * { box-sizing: border-box; margin: 0; padding: 0; }
  html, body { width: 1200px; height: 930px; overflow: hidden; }
  body {
    background: radial-gradient(circle at 45% 45%, #c8c8c8 0%, var(--bg) 70%);
    font-family: "Roboto", sans-serif;
    position: relative;
  }
  .card {
    position: absolute;
    width: 500px;
    height: 286px;
    border-radius: 18px;
    overflow: hidden;
    box-shadow: 0 10px 24px rgba(0,0,0,0.25);
  }
  .card-front { left: 120px; top: 110px; background: var(--blue); }
  .card-back { left: 580px; top: 520px; background: var(--white); }
  .fern-decoration {
    position: absolute;
    left: 40px; top: 0;
    width: 280px; height: 286px;
    background: radial-gradient(ellipse at 50% 60%, rgba(255,255,255,0.14) 0%, rgba(255,255,255,0) 70%);
  }
  .brand {
    position: absolute;
    display: flex;
    align-items: center;
    gap: 10px;
    font-family: "Montserrat", sans-serif;
    font-weight: 700;
    letter-spacing: 0.5px;
    white-space: nowrap;
    line-height: 1.2;
  }
  .brand-mark {
    width: 16px; height: 16px;
    border-radius: 50%;
    background: var(--orange);
    flex: none;
  }
  .card-front .brand { left: 100px; top: 118px; color: var(--white); font-size: 40px; }
  .card-back .brand { left: 28px; top: 88px; color: var(--blue); font-size: 28px; }
  .wave { position: absolute; inset: 0; width: 100%; height: 100%; }
  .person {
    position: absolute;
    right: 30px; top: 14px;
    text-align: right;
    line-height: 1.15;
  }
  .person-name {
    color: var(--blue);
    font-weight: 500;
    font-size: 19px;
    letter-spacing: 0.5px;
  }
  .person-role { color: var(--orange); font-size: 12px; margin-top: 1px; }
  .contact {
    position: absolute;
    right: 28px; top: 120px;
    text-align: right;
    color: var(--white);
    font-size: 12px;
    line-height: 1.45;
  }
  .contact .gap { margin-top: 8px; }
  .contact-line { display: flex; justify-content: flex-end; align-items: center; gap: 6px; }
  .contact-line svg { width: 10px; height: 10px; fill: var(--white); flex: none; }
</style>
</head>
<body>

<section class="card card-front" aria-label="Card front">
  <div class="fern-decoration" role="img" aria-label="Faint silver fern frond decoration"></div>
  <div class="brand"><span class="brand-mark"></span>ALVA Holdings</div>
</section>

<section class="card card-back" aria-label="Card back">
  <svg class="wave" viewBox="0 0 500 286" preserveAspectRatio="none" aria-hidden="true">
    <path d="M500,74 C410,74 340,95 305,155 C270,215 180,236 40,238 L0,238 L0,286 L500,286 Z" fill="var(--blue)"/>
    <path d="M500,58 C410,58 340,81 305,141 C270,201 180,220 40,222 L0,222" fill="none" stroke="var(--blue)" stroke-width="4"/>
    <path d="M0,226 L40,226 C180,224 270,203 305,143 C270,211 180,232 40,234 L0,234 Z" fill="var(--orange)"/>
  </svg>

  <div class="person">
    <div class="person-name">ROWAN HARTE</div>
    <div class="person-role">Director</div>
  </div>

  <div class="brand"><span class="brand-mark"></span>ALVA Holdings</div>

  <div class="contact">
    <div>42 Kauri Lane,</div>
    <div>Wellington, NZ, 6011</div>
    <div class="contact-line gap">(021) 555-0184
      <svg viewBox="0 0 10 10"><path d="M2 0.5 L3.8 2.6 L2.9 3.7 C3.6 5.2 4.8 6.4 6.3 7.1 L7.4 6.2 L9.5 8 L8.4 9.5 C4 9 1 6 0.5 1.6 Z"/></svg>
    </div>
    <div class="contact-line">info@alvaholdings.com
      <svg viewBox="0 0 10 10"><path d="M0.5 2 H9.5 V8 H0.5 Z M1.3 2.8 V7.2 H8.7 V2.8 L5 5.4 Z" fill-rule="evenodd"/></svg>
    </div>
    <div class="contact-line">www.alvaholdings.com
      <svg viewBox="0 0 10 10"><circle cx="5" cy="5" r="4.5"/></svg>
    </div>
  </div>
</section>

</body>
</html>
```